Briefpapier für Betrieb aus der Landwirtschaft
Zielgruppe
der Firmen name ist Brandol Jürgen
Wir sind ein Betrieb der aus der Landwirtschaft kommt und sich auf die bewirtschaftung von Streuobstäckern und wiesen spezialisiert hat.
Die Früchte der Bäume werden über eine von uns mitgegründete Genossenschaft vertrieben... Andere Früchte werden an destilierien und an Endverbraucher verkauft.
Zielgruppe:
Das Breifpapier soll für geschäftsbriefe rechnungen Lieferscheine, auftragsbestätigungen verwendung finden.
Und an Endkunden, Lieferanten und Geschaftspartner gehen !!
Wir haben ein Biolabel gegründet wiesel pur terra eventuell kann man sich an dem Logo orientieren !!
Aufgabenstellung
Ich habe unseren alten Briefbogen angehängt !!! Bitte nicht kopieren oder optimieren !!! Er ist nur da um die Daten zu nehmen !!! Briefpapier soll kompl. neu desingt werden... Firmen Name Brandol Jürgen
Ich brauche platz für die Biosiegel 2 in der Zahl
Frech / Modern eventuell mit wasserzeichen , hohen wiedererkennungswert.
Nach abschluss des desingns sollen Visitenkarten gemacht werden

```html
<!DOCTYPE html>
<html lang="de">
<head>
<meta charset="utf-8">
<title>Brandol Jürgen – Briefpapier</title>
<link href="https://fonts.googleapis.com/css2?family=Montserrat:wght@400;500;600&family=Arimo:wght@400;700&display=swap" rel="stylesheet">
<style>
  :root{
    --green-dark:#116a35;
    --green-mid:#2f8a2e;
    --green-lime:#8dc21f;
    --wash-light:#eef4dc;
    --wash-deep:#d6e6dc;
    --ink:#4a4a4a;
    --text:#111;
    --board:#9a9a9a;
    --paper:#fff;
  }
  *{box-sizing:border-box;margin:0;padding:0}
  html,body{width:1200px;height:720px;overflow:hidden}
  body{background:var(--board);position:relative;font-family:"Montserrat",sans-serif}
  .board-band{position:absolute;left:0;top:697px;width:1200px;height:23px;background:var(--green-lime);border-top:6px solid var(--paper)}
  .sheet{position:absolute;top:48px;width:433px;height:612px;background:var(--paper);overflow:hidden}
  .sheet--blank{left:113px}
  .sheet--letter{left:668px}
  .sheet__top{position:absolute;left:0;top:0;width:100%;height:11px;background:linear-gradient(90deg,var(--green-dark),var(--green-lime))}
  .sheet__bottom{position:absolute;left:0;bottom:0;width:100%;height:18px;background:linear-gradient(90deg,var(--green-lime),var(--green-dark))}
  .watermark{position:absolute;left:-40px;top:35px;width:480px;height:520px;border-radius:50%;
    background:radial-gradient(circle at 40% 30%,var(--wash-light) 0%,#e4eed6 45%,var(--wash-deep) 100%);opacity:.85}
  .brand{position:absolute;left:48px;top:45px;display:flex;align-items:center;gap:6px}
  .brand__dot{width:19px;height:19px;border-radius:50%;background:var(--green-mid)}
  .brand__name{font-weight:600;font-size:18.5px;color:var(--ink);letter-spacing:.3px}
  .sender-line{position:absolute;left:49px;top:98px;font-family:"Arimo",sans-serif;font-size:3.6px;color:#333;letter-spacing:.1px}
  .recipient{position:absolute;left:49px;top:111px;font-family:"Arimo",sans-serif;font-size:7.6px;line-height:8.8px;color:var(--text)}
  .subject{position:absolute;left:49px;top:236px;font-family:"Arimo",sans-serif;font-weight:700;font-size:7.6px;color:var(--text)}
  .salutation{position:absolute;left:49px;top:265px;font-family:"Arimo",sans-serif;font-size:7.6px;color:var(--text)}
  .body-text{position:absolute;left:49px;top:284px;width:330px;font-family:"Arimo",sans-serif;font-size:7.3px;line-height:9.6px;color:var(--text);text-align:justify}
  .footer{position:absolute;left:0;top:556px;width:100%;height:32px;font-size:5.4px;line-height:6.6px;color:#333}
  .footer__col{position:absolute;top:0;height:37px;border-left:1px solid var(--green-lime);padding-left:3px;padding-top:1px}
  .footer__col p+p{margin-top:4px}
  .col-name{left:46px}
  .col-contact{left:109px}
  .col-bank{left:195px}
  .col-label{left:297px;padding-left:5px;padding-top:4px}
  .label-name{font-weight:500;font-size:9px;line-height:8.4px;color:#4f6c5a;letter-spacing:.2px}
  .seal{position:absolute;left:374px;top:0;width:30px;height:29px;background:var(--green-mid)}
</style>
</head>
<body>

<section class="sheet sheet--blank" aria-label="Briefbogen leer">
  <div class="sheet__top"></div>
  <div class="watermark" role="img" aria-label="Zartes Blatt-Wasserzeichen in Hellgrün"></div>
  <div class="brand"><span class="brand__dot"></span><span class="brand__name">BRANDOL JÜRGEN</span></div>
  <p class="sender-line">Jürgen Brandol . Lindenhang 12 . 97311 Wiesbrunn OT Kaltental</p>
  <div class="footer">
    <div class="footer__col col-name"><p>Jürgen Brandol</p><p>Lindenhang 12<br>97311 Wiesbrunn<br>OT Kaltental</p></div>
    <div class="footer__col col-contact"><p>Fon +49 (0)9341 5528170<br>Fax +49 (0)9341 552819</p><p>kontakt@juergenbrandol.de<br>www.juergenbrandol.de</p></div>
    <div class="footer__col col-bank"><p>SteuerNr.: 418/903/55261</p><p>Bank&nbsp; Nordtal Bank<br>IBAN&nbsp; DE17300200118844201937<br>BIC&nbsp;&nbsp;&nbsp; NORTDEFFXXX</p></div>
    <div class="footer__col col-label"><p class="label-name">WIESEL PUR<br>TERRA</p></div>
    <div class="seal" role="img" aria-label="Biosiegel"></div>
  </div>
  <div class="sheet__bottom"></div>
</section>

<section class="sheet sheet--letter" aria-label="Briefbogen mit Mustertext">
  <div class="sheet__top"></div>
  <div class="watermark" role="img" aria-label="Zartes Blatt-Wasserzeichen in Hellgrün"></div>
  <div class="brand"><span class="brand__dot"></span><span class="brand__name">BRANDOL JÜRGEN</span></div>
  <p class="sender-line">Jürgen Brandol . Lindenhang 12 . 97311 Wiesbrunn OT Kaltental</p>
  <address class="recipient" style="font-style:normal">Firma<br>Herrn Max Mustermann<br>Straße Hausnummer<br>PLZ Ort</address>
  <p class="subject">Betreffszeile</p>
  <p class="salutation">Sehr geehrter Herr Mustermann,</p>
  <div class="body-text">
    <p>Iciuntur minctat reritas inctotae cusa quam, ut hillatemo incti simus sum ipiciliquia simi, nus quam aditatur mollitiatur?</p>
    <p>Ihit evenihillam, venimi, sumquid itaturiae plat quis con nis nem es volo que net pos nusci cum voluptur archilligent labor sumqui represtemo cum fugitat ibuscimusam erferum se natur?</p>
    <p>Ovitas ut porendigente nullabore, et mod eni te enest liciis quam si sunt, sam, cum ullias millorrumque dollatet que venda et ut volores erspici enduscias ma pos ut quiditiam ape nos doluptatur sae de aut essi digenis aut quodicia aut facestia quaepe sum volore net fugita culpa quae nis reperum quo mos num es dio. Et magnist volorerupis es atatem int assit quam rempele ssimoluptio velit, qui cum rate dolore ducipsa nisqui consed modit libus, totat parum, ius et eatem labo. Neque acea quassequi dolestr uptatist, si as quassit ectotatis dolor suntem re sinctiur? Oreperferae. Et arcidusda nia nam lantur am ipient voluptaquam volorio maxim quatatur, te non rest et qui id et occati nonsecea volorposant.</p>
    <p>Aximill estemque eos nonsentint apitem. Unda aliatus dignitatem la voluptat.</p>
    <p>Nemolum as ea dolorest fugia venes comnitam, totae. Tatur assequae consequiae ex elenihil modis a comnim duciend untibus, atende illabo. Fugianto culparc hillorp orerspe rsperibus maximin istentiatis endist, utatatur?</p>
    <p>Aximodio. Itates auditibus, iducima quis alit eaque venist quatque plaborem autatio mi, quod quatumquatur sita cumqui te ne nos apicit explignis sitam, nostrum eatia vel etum, sam reriam eiur antem quod qui que voluptatem rat porerias dolore iliaturio officab oratiae rem. Ad que nulloreiunt.</p>
    <p>Hendit, expel mi, sit lacest ella voluptas dolorer ciligent lab ium quo.</p>
    <p>Nat. Nobis volorrores idis duci doluptae asint.</p>
  </div>
  <div class="footer">
    <div class="footer__col col-name"><p>Jürgen Brandol</p><p>Lindenhang 12<br>97311 Wiesbrunn<br>OT Kaltental</p></div>
    <div class="footer__col col-contact"><p>Fon +49 (0)9341 5528170<br>Fax +49 (0)9341 552819</p><p>kontakt@juergenbrandol.de<br>www.juergenbrandol.de</p></div>
    <div class="footer__col col-bank"><p>SteuerNr.: 418/903/55261</p><p>Bank&nbsp; Nordtal Bank<br>IBAN&nbsp; DE17300200118844201937<br>BIC&nbsp;&nbsp;&nbsp; NORTDEFFXXX</p></div>
    <div class="footer__col col-label"><p class="label-name">WIESEL PUR<br>TERRA</p></div>
    <div class="seal" role="img" aria-label="Biosiegel"></div>
  </div>
  <div class="sheet__bottom"></div>
</section>

<div class="board-band"></div>
</body>
</html>
```